The Wellness Barn Business Card

Info for the front..... (in whichever order and layout looks best)
Tara Pellworth
Physiotherapist
4/38 Upper Ridgeway Rd
Dundowran
QLD 4655
0462875309
tarapellworth47@mailnest.com
www.thewelnesbarn.com.au
on the back I would like to be able to write appointments so probably just that heading with lines.
I like a sort of rustic style but mostly professional, colours in naturals, beige, brown, green etc. I dont mind if the logo colour is changed slightly to suit.

```html
<!DOCTYPE html>
<html lang="en">
<head>
<meta charset="utf-8">
<title>The Wellness Barn – Business Card</title>
<link href="https://fonts.googleapis.com/css2?family=Montserrat:wght@400;500;700;800&display=swap" rel="stylesheet">
<style>
  :root {
    --bg: #3b3b3b;
    --card: #ffffff;
    --green: #2f3f22;
    --ink: #1f1f1f;
    --rule: #3d4a30;
  }
  * { margin: 0; padding: 0; box-sizing: border-box; }
  html, body { width: 1200px; height: 875px; overflow: hidden; }
  body {
    background: var(--bg);
    font-family: "Montserrat", sans-serif;
    position: relative;
  }
  .card {
    position: absolute;
    top: 272px;
    width: 540px;
    height: 330px;
    background: var(--card);
    border-radius: 22px;
    border-bottom: 6px solid var(--green);
    overflow: hidden;
  }
  .card--back { left: 40px; }
  .card--front { left: 620px; }

  .brand {
    position: absolute;
    top: 34px;
    right: 34px;
    display: flex;
    align-items: center;
    gap: 10px;
  }
  .brand__dot {
    width: 16px; height: 16px;
    border-radius: 50%;
    background: var(--green);
  }
  .brand__name {
    font-weight: 800;
    font-size: 22px;
    color: var(--green);
    letter-spacing: 0.2px;
  }
  .brand-rule {
    position: absolute;
    top: 84px;
    right: 34px;
    width: 300px;
    border-top: 1px solid var(--rule);
  }

  /* appointment side */
  .appt__title {
    position: absolute;
    left: 34px;
    top: 118px;
    font-weight: 700;
    font-size: 22px;
    color: var(--green);
    padding-bottom: 4px;
    border-bottom: 1px solid var(--rule);
  }
  .appt__row {
    position: absolute;
    left: 34px;
    right: 34px;
    display: flex;
    align-items: flex-end;
    gap: 8px;
    font-weight: 700;
    font-size: 14px;
    color: var(--green);
  }
  .appt__row--name { top: 180px; }
  .appt__row--date { top: 222px; }
  .appt__line {
    flex: 1;
    border-bottom: 1px solid var(--rule);
    height: 14px;
  }
  .appt__line--short { flex: 0.9; }
  .appt__note {
    position: absolute;
    left: 34px;
    right: 24px;
    top: 274px;
    font-weight: 700;
    font-size: 10.6px;
    letter-spacing: -0.1px;
    white-space: nowrap;
    color: var(--green);
  }

  /* contact side */
  .address {
    position: absolute;
    right: 34px;
    top: 104px;
    text-align: right;
    font-size: 13px;
    line-height: 1.35;
    color: var(--ink);
  }
  .person__name {
    position: absolute;
    left: 34px;
    top: 152px;
    font-weight: 700;
    font-size: 24px;
    color: var(--green);
    line-height: 1.1;
  }
  .name-rule {
    position: absolute;
    left: 34px;
    right: 34px;
    top: 186px;
    border-top: 1px solid var(--rule);
  }
  .person__role {
    position: absolute;
    left: 34px;
    top: 194px;
    font-size: 14px;
    color: var(--ink);
  }
  .contact {
    position: absolute;
    left: 34px;
    top: 222px;
    list-style: none;
  }
  .contact__item {
    display: flex;
    align-items: center;
    gap: 10px;
    font-size: 13.5px;
    color: var(--ink);
    margin-bottom: 8px;
  }
  .contact__icon { width: 14px; height: 14px; fill: var(--green); flex: none; }
</style>
</head>
<body>

  <section class="card card--back" aria-label="Appointment side">
    <div class="brand">
      <span class="brand__dot"></span>
      <span class="brand__name">The Wellness Barn</span>
    </div>
    <div class="brand-rule"></div>

    <h2 class="appt__title">Appoinment</h2>
    <div class="appt__row appt__row--name">
      <span>Name:</span><span class="appt__line"></span>
    </div>
    <div class="appt__row appt__row--date">
      <span>Date:</span><span class="appt__line"></span>
      <span>Time:</span><span class="appt__line appt__line--short"></span>
      <span>am/pm</span>
    </div>
    <p class="appt__note">If your unable to keep your appoinment. Please contact us as soon as possible</p>
  </section>

  <section class="card card--front" aria-label="Contact side">
    <div class="brand">
      <span class="brand__dot"></span>
      <span class="brand__name">The Wellness Barn</span>
    </div>
    <div class="brand-rule"></div>

    <p class="address">4/38 Upper Ridgeway Rd<br>Kestrelvale QLD 4871</p>

    <h1 class="person__name">Tara Pellworth</h1>
    <div class="name-rule"></div>
    <p class="person__role">Physiotherapist</p>

    <ul class="contact">
      <li class="contact__item">
        <svg class="contact__icon" viewBox="0 0 24 24"><path d="M6.6 10.8a15.1 15.1 0 0 0 6.6 6.6l2.2-2.2a1 1 0 0 1 1-.25 11.4 11.4 0 0 0 3.6.57 1 1 0 0 1 1 1V20a1 1 0 0 1-1 1A17 17 0 0 1 3 4a1 1 0 0 1 1-1h3.5a1 1 0 0 1 1 1c0 1.25.2 2.45.57 3.6a1 1 0 0 1-.25 1z"/></svg>
        0462875309
      </li>
      <li class="contact__item">
        <svg class="contact__icon" viewBox="0 0 24 24"><path d="M2 5h20v14H2z M2 5l10 8 10-8" fill="none" stroke="#2f3f22" stroke-width="2"/></svg>
        tarapellworth47@mailnest.com
      </li>
      <li class="contact__item">
        <svg class="contact__icon" viewBox="0 0 24 24"><circle cx="12" cy="12" r="9" fill="none" stroke="#2f3f22" stroke-width="2"/><path d="M3 12h18M12 3c3 3 3 15 0 18M12 3c-3 3-3 15 0 18" fill="none" stroke="#2f3f22" stroke-width="1.6"/></svg>
        www.thewelnesbarn.com.au
      </li>
    </ul>
  </section>

</body>
</html>
```